ZEK Stationaty Design
ZEK Protection
Project: ZEK Stationaty Design
ZEK Stationaty Design - Security
Creative Brief
Use specific fonts
Agency FB
Professional
Marco VEDI
Directeur
9 Chemin des Tilleuls 1299 Clairval-sur-Lac Suisse
info@zek-protection.example
www.zek-protection.example
Tom482 Tom482
Dear Fraktalgrafik, Vorlo, Thank you for your top designs. We have selected the preferred one with 4 & 5 stars. Could you please submit designs with the top selected business card, and add a A4 page and a email signature designs as well please, any additional stationery design will be great. Thank you in advance, Best regards, Tom

```html
<!DOCTYPE html>
<html lang="fr">
<head>
<meta charset="utf-8">
<title>ZEK Protection – Business Card</title>
<link rel="stylesheet" href="https://fonts.googleapis.com/css2?family=Roboto+Condensed:wght@400;700&display=swap">
<style>
  :root {
    --stage: #e9e7e3;
    --card-black: #141414;
    --card-black-edge: #262626;
    --card-white: #ffffff;
    --brand-red: #c8141c;
    --brand-red-dark: #7a0a0f;
    --ink: #2b2b2b;
    --silver: #9a9a9a;
    --text-light: #ffffff;
  }
  * { margin: 0; padding: 0; box-sizing: border-box; }
  html, body {
    width: 1200px; height: 904px; overflow: hidden;
    background: var(--stage);
    font-family: "Roboto Condensed", Arial, sans-serif;
  }
  .canvas { position: relative; width: 1200px; height: 904px; }
  .card {
    position: absolute; width: 700px; height: 400px;
    overflow: hidden; box-shadow: 0 12px 28px rgba(0,0,0,.25);
  }
  .card--back {
    left: 60px; top: 50px;
    background: radial-gradient(circle at 50% 45%, var(--card-black-edge), var(--card-black) 70%);
    display: flex; align-items: center; justify-content: center;
  }
  .card--front { left: 440px; top: 454px; background: var(--card-white); }

  .brand-mark { display: flex; align-items: center; gap: 14px; }
  .brand-mark__dot {
    width: 110px; height: 110px; border-radius: 50%; background: var(--silver); flex: none;
  }
  .brand-mark__name {
    font-weight: 700; font-size: 30px; color: var(--text-light); letter-spacing: 1px;
  }
  .card--front .brand-mark { position: absolute; left: 40px; top: 150px; }
  .card--front .brand-mark__dot { width: 120px; height: 120px; background: #3a3a3a; }
  .card--front .brand-mark__name { color: var(--brand-red); font-size: 26px; margin-top: 40px; }

  .header-swoosh { position: absolute; left: 0; top: 0; width: 700px; height: 400px; }

  .person { position: absolute; right: 40px; top: 28px; text-align: right; }
  .person__name { color: var(--brand-red); font-size: 22px; }
  .person__role { color: var(--text-light); font-size: 15px; margin-top: 2px; }

  .address {
    position: absolute; left: 40px; bottom: 36px;
    color: var(--ink); font-size: 17px; line-height: 1.3; font-style: normal;
  }
  .contacts {
    position: absolute; right: 40px; top: 186px; list-style: none;
    color: var(--ink); font-size: 16px; line-height: 1;
  }
  .contacts li { display: flex; align-items: center; gap: 8px; margin-bottom: 7px; }
  .contacts svg { width: 14px; height: 14px; fill: var(--brand-red); flex: none; }
</style>
</head>
<body>
<main class="canvas">

  <section class="card card--back" aria-label="Card back">
    <div class="brand-mark">
      <span class="brand-mark__dot"></span>
      <span class="brand-mark__name">ZEK Protection</span>
    </div>
  </section>

  <section class="card card--front" aria-label="Card front">
    <svg class="header-swoosh" viewBox="0 0 700 400" aria-hidden="true">
      <defs>
        <linearGradient id="redBand" x1="0" y1="0" x2="1" y2="0">
          <stop offset="0" stop-color="#7a0a0f"/>
          <stop offset=".5" stop-color="#c8141c"/>
          <stop offset="1" stop-color="#7a0a0f"/>
        </linearGradient>
      </defs>
      <path d="M0 0 H700 V138 C520 110 300 96 0 150 Z" fill="url(#redBand)"/>
      <path d="M0 0 H700 V124 C520 96 300 82 0 136 Z" fill="#141414"/>
    </svg>

    <div class="brand-mark">
      <span class="brand-mark__dot"></span>
      <span class="brand-mark__name">ZEK</span>
    </div>

    <div class="person">
      <p class="person__name">Marco VEDI</p>
      <p class="person__role">Directeur</p>
    </div>

    <ul class="contacts">
      <li><svg viewBox="0 0 16 16"><path d="M3 1h3l1 4-2 1a9 9 0 0 0 5 5l1-2 4 1v3a2 2 0 0 1-2 2A13 13 0 0 1 1 3a2 2 0 0 1 2-2z"/></svg>+41 22 555 01 10</li>
      <li><svg viewBox="0 0 16 16"><rect x="4" y="1" width="8" height="14" rx="1.5"/></svg>+41 79 555 02 20</li>
      <li><svg viewBox="0 0 16 16"><rect x="1" y="5" width="14" height="8" rx="1"/><rect x="4" y="1" width="8" height="4"/></svg>+41 22 555 03 30</li>
      <li><svg viewBox="0 0 16 16"><path d="M1 3h14v10H1z M1 3l7 6 7-6"/></svg>info@zek-protection.example</li>
      <li><svg viewBox="0 0 16 16"><circle cx="8" cy="8" r="7"/></svg>www.zek-protection.example</li>
    </ul>

    <address class="address">
      9 Chemin des Tilleuls<br>
      1299 Clairval-sur-Lac<br>
      Suisse
    </address>
  </section>

</main>
</body>
</html>
```